Business Card Design Project

Corvexa logo will be provided after
Front

Bram Oskarsen- Construction Manager

Ph: (61) 07 53182907
boskarsen@corvexa.com.au
PO Box 83 Kelbarra 4529

Back
Corvexa
EPCM

Oil - Gas - Mining

Industry/Entity Type

Business

Font styles to use
Sans Serif

Colors
faa54b

Requirements
Must have
• White Back Ground

```html
<!DOCTYPE html>
<html lang="en">
<head>
<meta charset="utf-8">
<title>Corvexa Business Card</title>
<link rel="stylesheet" href="https://fonts.googleapis.com/css2?family=Arimo&family=Oswald:wght@300&display=swap">
<style>
  :root {
    --page: #ffffff;
    --mat: #ffffff;
    --mat-edge: #000000;
    --card-back: #000000;
    --card-front: #cbcbcb;
    --accent: #ef7d1f;
  }
  * { margin: 0; padding: 0; box-sizing: border-box; }
  html, body {
    width: 1096px;
    height: 1200px;
    overflow: hidden;
    background: var(--page);
  }
  .canvas {
    position: relative;
    width: 1096px;
    height: 1200px;
  }
  .mat {
    position: absolute;
    left: 25px;
    top: 0;
    width: 683px;
    height: 858px;
    background: var(--mat);
    border: 1px solid var(--mat-edge);
  }
  .card {
    position: absolute;
    left: 112px;
    width: 525px;
    height: 338px;
  }
  .card--back { top: 72px; background: var(--card-back); }
  .card--front { top: 428px; background: var(--card-front); }

  .text {
    position: absolute;
    color: var(--accent);
    white-space: nowrap;
    line-height: 1;
  }
  .condensed { font-family: "Oswald", sans-serif; font-weight: 300; }
  .sans { font-family: "Arimo", sans-serif; }
  .centered { left: 0; width: 100%; text-align: center; }

  .brand-name { top: 110px; font-size: 54px; left: -13px; }
  .brand-tag { top: 173px; left: -13px; font-size: 23px; }
  .brand-sectors { top: 206px; left: -13px; font-size: 15px; }

  .person-name { top: 96px; left: -10px; font-size: 51px; }
  .person-role { top: 152px; left: -10px; font-size: 16px; }

  .phone { left: 47px; top: 238px; font-size: 20px; }
  .email { left: 46px; top: 259px; font-size: 18px; }
  .postal { left: 316px; top: 237px; font-size: 18px; }
</style>
</head>
<body>
  <main class="canvas">
    <div class="mat"></div>

    <section class="card card--back" aria-label="Card back">
      <div class="text condensed centered brand-name">Corvexa</div>
      <div class="text sans centered brand-tag">EPCM</div>
      <div class="text sans centered brand-sectors">Oil - Gas - Mining</div>
    </section>

    <section class="card card--front" aria-label="Card front">
      <div class="text condensed centered person-name">Bram Oskarsen</div>
      <div class="text condensed centered person-role">Construction Manager</div>
      <div class="text condensed phone">Ph: (61) 07 53182907</div>
      <div class="text condensed email">boskarsen@corvexa.com.au</div>
      <div class="text condensed postal">PO Box 83 Kelbarra 4529</div>
    </section>
  </main>
</body>
</html>
```